Valdorra Holdings Real Estate Company business cards

New business card design, we are generally happy with the basic layout of the existing front of business card, (feel free to change) but require a head shot photo on the back side.

http://www.valdorra.com.au/

Attached logos, and existing business card

------------------------------

Target Market(s)

Real estate

Industry/Entity Type

Real Estate

Contact Information for Business Card

Standard size double sided

Font styles to use
Other font styles liked:
• Futura

Requirements
Must have
• Photo head shot on the back side
Nice to have
• yes
Should not have
• No

```html
<!DOCTYPE html>
<html lang="en">
<head>
<meta charset="UTF-8">
<title>Valdorra Holdings – Business Cards</title>
<link rel="stylesheet" href="https://fonts.googleapis.com/css2?family=Jost:wght@400;500;600&display=swap">
<style>
  :root {
    --page: #e6e4ea;
    --card: #35206e;
    --white: #ffffff;
    --soft: #e9e6f3;
    --accent: #f39323;
    --photo-top: #e7e8ea;
    --photo-bottom: #3a4060;
  }
  * { box-sizing: border-box; margin: 0; padding: 0; }
  html, body { width: 1200px; height: 900px; overflow: hidden; }
  body {
    background: var(--page);
    font-family: 'Jost', sans-serif;
    color: var(--white);
    position: relative;
  }
  .card {
    position: absolute;
    left: 250px;
    width: 700px;
    height: 400px;
    background: var(--card);
    box-shadow: 0 8px 24px rgba(30, 20, 60, 0.25);
  }
  .card--front { top: 35px; }
  .card--back { top: 465px; }

  .wordmark {
    font-weight: 500;
    color: var(--white);
    letter-spacing: 1px;
    line-height: 1;
  }
  .card--front .wordmark {
    position: absolute;
    top: 95px;
    left: 0;
    width: 100%;
    text-align: center;
    font-size: 64px;
  }
  .services {
    position: absolute;
    top: 235px;
    left: 0;
    width: 100%;
    display: flex;
    justify-content: center;
    gap: 28px;
    font-size: 32px;
    font-weight: 600;
  }

  .headshot-frame {
    position: absolute;
    left: 55px;
    top: 60px;
    width: 300px;
    height: 300px;
    border: 3px solid var(--white);
  }
  .headshot {
    width: 100%;
    height: 100%;
    background: linear-gradient(180deg, var(--photo-top) 0%, var(--photo-top) 45%, var(--photo-bottom) 100%);
  }
  .card--back .wordmark {
    position: absolute;
    top: 38px;
    left: 385px;
    font-size: 52px;
  }
  .details {
    position: absolute;
    left: 388px;
    top: 150px;
    width: 300px;
  }
  .person { font-size: 23px; font-weight: 600; }
  .person .role { font-weight: 400; color: var(--soft); }
  .company { margin-top: 26px; font-size: 21px; font-weight: 600; line-height: 1.1; }
  .abn { font-size: 17px; font-weight: 400; color: var(--soft); }
  .contact { list-style: none; margin-top: 34px; }
  .contact li { display: flex; align-items: center; gap: 10px; font-size: 18px; height: 28px; }
  .contact .phone { font-size: 22px; font-weight: 600; letter-spacing: 1px; }
  .contact .web { margin-top: 26px; }
  .icon { width: 22px; height: 22px; flex: none; }
</style>
</head>
<body>
  <section class="card card--front">
    <div class="wordmark">valdorra</div>
    <div class="services"><span>Buy</span><span>|</span><span>Sell</span><span>|</span><span>Rent</span></div>
  </section>

  <section class="card card--back">
    <div class="headshot-frame">
      <div class="headshot" role="img" aria-label="Head shot photo of the director in suit and tie"></div>
    </div>
    <div class="wordmark">valdorra</div>
    <div class="details">
      <p class="person">Marcus Ellery <span class="role">| Director</span></p>
      <p class="company">Valdorra Holdings<br><span class="abn">ABN: 12 345 678 901</span></p>
      <ul class="contact">
        <li class="phone">
          <svg class="icon" viewBox="0 0 22 22"><circle cx="11" cy="11" r="11" fill="#f39323"/><path d="M7.5 6c.6-.5 1.3-.3 1.6.3l.8 1.6c.2.5 0 1-.4 1.3l-.6.4c.6 1.4 1.6 2.4 3 3l.4-.6c.3-.4.8-.6 1.3-.4l1.6.8c.6.3.8 1 .3 1.6l-.7.8c-.6.6-1.6.7-2.6.2-2.3-1.1-4-2.8-5.1-5.1-.5-1-.4-2 .2-2.6z" fill="#fff"/></svg>
          0400 555 318
        </li>
        <li>
          <svg class="icon" viewBox="0 0 22 22"><circle cx="11" cy="11" r="11" fill="#f39323"/><rect x="5.5" y="7" width="11" height="8" fill="#fff"/><path d="M5.5 7l5.5 4.5L16.5 7" fill="none" stroke="#f39323" stroke-width="1.2"/></svg>
          marcus.ellery@valdorra.com.au
        </li>
        <li class="web">
          <svg class="icon" viewBox="0 0 22 22"><circle cx="11" cy="11" r="11" fill="#f39323"/><g fill="none" stroke="#fff" stroke-width="1.2"><circle cx="11" cy="11" r="6"/><ellipse cx="11" cy="11" rx="2.6" ry="6"/><path d="M5 11h12M6 8h10M6 14h10"/></g></svg>
          www.valdorra.com.au
        </li>
      </ul>
    </div>
  </section>
</body>
</html>
```